I need a wine label for a new winery called "Chateau Verelline".
I am looking for an old french style label with a sketched image of a vineyard with the goat with the missing horn somewhat discreetly in the image. Also I want the label to read in much smaller print "Quiet Brook Vineyards". Perhaps in a courtyard the goat with the missing horn is kneeling beside an old wine press. Please see images for examples. P.S. "Verelline" is the goat that fed baby Zeus in mythology. He broke off her horn and it became the horn of pleanty (cornucopia).

Industry/Entity Type

Vineyard

Font styles to use
Script

Requirements
Must have
• sketched image on an off white/white/yellow label
Nice to have
• Nice to have the vineyard with the goat missing a horn kneeling by the old wine press

```html
<!DOCTYPE html>
<html lang="en">
<head>
<meta charset="utf-8">
<title>Chateau Verelline – Cabernet Sauvignon Label</title>
<link rel="stylesheet" href="https://fonts.googleapis.com/css2?family=EB+Garamond:ital,wght@0,400;0,500;1,400;1,500&display=swap">
<style>
  :root {
    --page-bg: #f6f4ee;
    --label-cream: #f6f0de;
    --label-cream-light: #f9f5e8;
    --frame-tan: #c8b095;
    --ink-dark: #2f2b28;
    --ink-mid: #5a534d;
    --ink-soft: #77706a;
    --vintage-rust: #a34e2b;
    --sketch-sepia: #8a7560;
    --sketch-fade: #efe7d3;
  }
  * { margin: 0; padding: 0; box-sizing: border-box; }
  html, body {
    width: 1200px; height: 1200px; overflow: hidden;
    background: var(--page-bg);
  }
  .canvas { position: relative; width: 1200px; height: 1200px; }

  .wine-label {
    position: absolute; left: 294px; top: 50px;
    width: 612px; height: 1100px;
    background: linear-gradient(180deg, var(--label-cream-light) 0%, var(--label-cream) 100%);
    font-family: "EB Garamond", Georgia, serif;
    color: var(--ink-dark);
    text-align: center;
    box-shadow: 0 1px 3px rgba(0,0,0,0.06);
  }
  .label-frame {
    position: absolute; inset: 16px;
    border: 3px solid var(--frame-tan);
  }
  .label-frame::after {
    content: ""; position: absolute; inset: 4px;
    border: 1px solid var(--frame-tan); opacity: 0.6;
  }

  .estate-name {
    position: absolute; left: 0; right: 0; top: 118px;
    font-style: italic; font-weight: 400;
    font-size: 104px; line-height: 100px;
    letter-spacing: -1px;
    color: var(--ink-dark);
  }
  .estate-name span { display: block; }

  .vineyard-sketch {
    position: absolute; left: 72px; top: 412px;
    width: 464px; height: 330px;
    background: radial-gradient(ellipse at 50% 50%, var(--sketch-sepia) 0%, #b6a28b 40%, var(--sketch-fade) 72%, rgba(246,240,222,0) 100%);
    opacity: 0.55;
  }

  .vintage {
    position: absolute; left: 0; right: 0; top: 808px;
    font-size: 21px; letter-spacing: 0.5px;
    color: var(--vintage-rust);
  }
  .varietal {
    position: absolute; left: 0; right: 0; top: 862px;
    font-size: 34px; letter-spacing: 1.5px;
    font-variant: small-caps; color: var(--ink-dark);
  }
  .vineyard-name {
    position: absolute; left: 0; right: 0; top: 948px;
    font-size: 22px; letter-spacing: 1.5px;
    color: var(--ink-mid);
  }
  .region {
    position: absolute; left: 0; right: 0; top: 988px;
    font-size: 18px; letter-spacing: 1.5px;
    color: var(--ink-mid);
  }
  .fine-print {
    position: absolute; top: 1047px;
    font-size: 15px; color: var(--ink-soft);
  }
  .fine-print.alcohol { left: 36px; }
  .fine-print.volume { right: 42px; }
</style>
</head>
<body>
<div class="canvas">
  <section class="wine-label">
    <div class="label-frame"></div>

    <h1 class="estate-name"><span>Chateau</span><span>Verelline</span></h1>

    <div class="vineyard-sketch" role="img" aria-label="Sepia pen sketch of a vineyard with hills, a one-horned goat lying beside an old wooden wine press"></div>

    <p class="vintage">VINTAGE 2016</p>
    <p class="varietal">Cabernet Sauvignon</p>
    <p class="vineyard-name">QUIET BROOK VINEYARDS</p>
    <p class="region">AMBER RIDGEVALE</p>

    <p class="fine-print alcohol">NO ALCOHOL %</p>
    <p class="fine-print volume">370ml</p>
  </section>
</div>
</body>
</html>
```